Request for Business Card Design

Hi. My name is Marlena, I am looking for a new business card design for my company, Quillbrook Sensing Systems, LLC. I really like the design you did for Tavel Harvest and was hoping you could do something similar using our full logo and our mark. I am also open to any raised texture design using our mark. I have attached our full logo, which would need to be somewhere on the card, as well as the mark in both outline and full form, as well as our brand colors / guide. The card does not have to be white, as long as our logo and mark appear. I actually like darker colored business cards more, but am open to all options. If you are interested in working with me, please let me know. We would also take the business card design into letterhead design if you can do that.

```html
<!DOCTYPE html>
<html lang="en">
<head>
<meta charset="utf-8">
<title>Quillbrook Sensing Systems — Business Card</title>
<link rel="stylesheet" href="https://fonts.googleapis.com/css2?family=Barlow:wght@400;500;600&family=Montserrat:wght@700&display=swap">
<style>
  :root {
    --backdrop-light: #ececec;
    --backdrop-dark: #b9b9b9;
    --card-dark: #211e1f;
    --card-mid: #3a3738;
    --brand-blue: #3aa6cc;
    --ink-white: #f4f4f4;
  }
  * { box-sizing: border-box; margin: 0; padding: 0; }
  html, body {
    width: 1200px; height: 1200px; overflow: hidden;
  }
  body {
    background: linear-gradient(120deg, var(--backdrop-light) 0%, var(--backdrop-dark) 100%);
    font-family: "Barlow", Arial, sans-serif;
    color: var(--ink-white);
    position: relative;
  }
  .card {
    position: absolute;
    width: 760px; height: 434px;
    border-radius: 26px;
    background: linear-gradient(135deg, var(--card-mid) 0%, var(--card-dark) 55%, var(--card-dark) 100%);
    box-shadow: 0 6px 0 #0e0d0d, 0 18px 30px rgba(0,0,0,0.25);
  }
  .card-front { left: 120px; top: 110px; }
  .card-back { left: 320px; top: 650px; }

  .brand {
    position: absolute;
    display: flex; align-items: center; gap: 22px;
  }
  .brand-dot {
    border-radius: 50%;
    background: var(--brand-blue);
    flex: none;
  }
  .brand-name {
    font-weight: 600;
    letter-spacing: 0.06em;
    text-transform: uppercase;
    color: var(--ink-white);
    line-height: 1.05;
  }
  .card-front .brand { left: 110px; top: 150px; }
  .card-front .brand-dot { width: 96px; height: 96px; }
  .card-front .brand-name { font-size: 44px; }

  .website {
    position: absolute; left: 0; right: 0; bottom: 60px;
    text-align: center;
    font-size: 22px; font-weight: 500; letter-spacing: 0.04em;
  }
  .website .domain { color: var(--brand-blue); }

  .card-back .brand { right: 50px; top: 50px; gap: 16px; }
  .card-back .brand-dot { width: 56px; height: 56px; }
  .card-back .brand-name { font-size: 26px; }

  .person { position: absolute; left: 70px; bottom: 62px; }
  .person-name {
    font-family: "Montserrat", Arial, sans-serif;
    font-size: 30px; color: var(--brand-blue);
  }
  .person-role { font-size: 21px; margin: 2px 0 14px 8px; letter-spacing: 0.03em; }
  .contact-list { list-style: none; margin-left: 8px; }
  .contact-list li {
    display: flex; align-items: center; gap: 14px;
    font-size: 21px; letter-spacing: 0.04em; line-height: 1.4;
  }
  .contact-list svg { width: 20px; height: 20px; fill: var(--brand-blue); flex: none; }

  .address {
    position: absolute; right: 50px; bottom: 110px;
    text-align: right; font-size: 21px; letter-spacing: 0.04em; line-height: 1.35;
  }
</style>
</head>
<body>
  <section class="card card-front">
    <div class="brand">
      <span class="brand-dot"></span>
      <span class="brand-name">Quillbrook<br>Sensing Systems</span>
    </div>
    <p class="website">www.<span class="domain">quillbrooksensing</span>.com</p>
  </section>

  <section class="card card-back">
    <div class="brand">
      <span class="brand-dot"></span>
      <span class="brand-name">Quillbrook<br>Sensing Systems</span>
    </div>

    <div class="person">
      <h1 class="person-name">Marlena</h1>
      <p class="person-role">Founder &amp; Director</p>
      <ul class="contact-list">
        <li>
          <svg viewBox="0 0 24 24" aria-hidden="true"><path d="M6.6 10.8a15.1 15.1 0 0 0 6.6 6.6l2.2-2.2c.3-.3.7-.4 1-.2 1.1.4 2.3.6 3.6.6.6 0 1 .4 1 1V20c0 .6-.4 1-1 1A17 17 0 0 1 3 4c0-.6.4-1 1-1h3.5c.6 0 1 .4 1 1 0 1.3.2 2.5.6 3.6.1.3 0 .7-.2 1z"/></svg>
          +001 555 210 4418
        </li>
        <li>
          <svg viewBox="0 0 24 24" aria-hidden="true"><path d="M7 3h10v5H7zM4 9h16a2 2 0 0 1 2 2v6h-4v4H6v-4H2v-6a2 2 0 0 1 2-2zm4 7v3h8v-3z"/></svg>
          +001 555 210 4419
        </li>
        <li>
          <svg viewBox="0 0 24 24" aria-hidden="true"><path d="M2 5h20v14H2zm2 2v.5l8 5 8-5V7z"/></svg>
          info@quillbrooksensing.com
        </li>
      </ul>
    </div>

    <p class="address">1180 Harbor Mill Road.<br>Fernvale, CO 80999</p>
  </section>
</body>
</html>
```